Business Card Design Project

looking for a stylish and simple double sided business card.
I am an artist - specialising in fashion illustration, portraits and murals.
the front should be simply my name and tag:

D U R E S K
Bold in colour

My preference is for a Black background with DURESK in red or embossed.
Bold in colour in White or multi-coloured.

the back will have detail:

Personalised Art
Portraits, Murals, Fashion Illustration

0437 582 190
duresk@duresk.com.au
www.duresk.com.au

Target Market(s)

Adults that are based in western speaking countries who have an appreciation for art and design. Portraits and wall art
Business owners who may need personalised all art for their business space. Murals and personalised canvass.
People in the fashion industry, who may require fashion illustrations.

Industry/Entity Type

Fashion

Requirements
Must have
• BOLD but simple at the same time, timeless modern element to it.
Nice to have
• simple lettering
Should not have
• Not too busy or wordy,

```html
<!DOCTYPE html>
<html lang="en">
<head>
<meta charset="utf-8">
<title>Duresk – Business Card</title>
<link rel="stylesheet" href="https://fonts.googleapis.com/css2?family=Arimo:wght@700&family=Cinzel:wght@600&family=Michroma&family=Tinos:ital,wght@0,700;1,700&display=swap">
<style>
  :root {
    --backdrop: #2a2a2c;
    --red: #e3190f;
    --red-deep: #b80f0a;
    --red-dark: #8e0b08;
    --paper: #f4f4f4;
    --paper-shade: #dcdcdc;
    --ink-grey: #4a4a4a;
    --silver: #f2f2f2;
    --white: #ffffff;
  }
  * { margin: 0; padding: 0; box-sizing: border-box; }
  html, body {
    width: 1200px; height: 900px; overflow: hidden;
    background: var(--backdrop);
  }
  .canvas {
    width: 1200px; height: 900px;
    display: flex; flex-direction: column; align-items: center; justify-content: center;
    gap: 30px;
  }
  .card {
    position: relative;
    width: 700px; height: 400px;
    overflow: hidden;
    box-shadow: 0 10px 30px rgba(0,0,0,.5);
  }
  .card-bg { position: absolute; inset: 0; width: 100%; height: 100%; }

  /* Front */
  .front .wordmark {
    position: absolute; left: 0; right: 0; top: 150px;
    text-align: center;
    font-family: "Arimo", sans-serif; font-weight: 700;
    font-size: 88px; letter-spacing: 32px; padding-left: 32px;
    color: var(--red);
    line-height: 1;
  }
  .front .tagline {
    position: absolute; left: 0; right: 0; top: 258px;
    text-align: center;
    font-family: "Tinos", serif; font-weight: 700;
    font-size: 30px; letter-spacing: 2px; word-spacing: 28px;
    color: var(--ink-grey);
    line-height: 1;
  }

  /* Back */
  .back .wordmark {
    position: absolute; left: 0; right: 0; top: 150px;
    text-align: center;
    font-family: "Cinzel", serif; font-weight: 600;
    font-size: 30px; letter-spacing: 14px; padding-left: 14px;
    color: var(--silver);
  }
  .back .details {
    position: absolute; left: 62px; top: 208px;
    color: var(--white);
  }
  .back .service {
    font-family: "Michroma", sans-serif;
    font-size: 24px; letter-spacing: 1px;
    margin-bottom: 8px;
  }
  .back .specialties {
    font-family: "Tinos", serif; font-style: italic; font-weight: 700;
    font-size: 15px; letter-spacing: .5px; text-transform: uppercase;
    margin-bottom: 12px;
  }
  .back .contact {
    list-style: none;
    font-family: "Tinos", serif; font-weight: 700;
    font-size: 17px; line-height: 26px;
  }
</style>
</head>
<body>
<main class="canvas">

  <section class="card front">
    <svg class="card-bg" viewBox="0 0 700 400" preserveAspectRatio="none" aria-hidden="true">
      <defs>
        <linearGradient id="paperGrad" x1="0" y1="0" x2="1" y2="1">
          <stop offset="0" stop-color="#ffffff"/>
          <stop offset="1" stop-color="#e2e2e2"/>
        </linearGradient>
        <linearGradient id="frontRed" x1="0" y1="0" x2="1" y2="1">
          <stop offset="0" stop-color="#e3190f"/>
          <stop offset="1" stop-color="#b80f0a"/>
        </linearGradient>
      </defs>
      <rect width="700" height="400" fill="url(#paperGrad)"/>
      <polygon points="0,300 700,250 700,400 0,400" fill="#d6d6d6" opacity=".5"/>
      <polygon points="0,330 700,235 700,400 0,400" fill="url(#frontRed)"/>
      <polygon points="0,370 700,270 700,300 0,400" fill="#ffffff" opacity=".08"/>
      <polygon points="180,0 400,0 400,70 340,95 180,95" fill="var(--red)"/>
    </svg>
    <h1 class="wordmark">DURESK</h1>
    <p class="tagline">Bold in colour</p>
  </section>

  <section class="card back">
    <svg class="card-bg" viewBox="0 0 700 400" preserveAspectRatio="none" aria-hidden="true">
      <defs>
        <linearGradient id="backRed" x1="0" y1="0" x2="1" y2="1">
          <stop offset="0" stop-color="#e3190f"/>
          <stop offset="1" stop-color="#8e0b08"/>
        </linearGradient>
      </defs>
      <rect width="700" height="400" fill="url(#backRed)"/>
      <polygon points="0,260 700,150 700,210 0,330" fill="#ffffff" opacity=".05"/>
      <polygon points="150,400 700,220 700,300 320,400" fill="#000000" opacity=".08"/>
      <polygon points="0,360 480,200 700,260 700,400 0,400" fill="#000000" opacity=".06"/>
      <polygon points="262,0 458,0 458,76 392,104 262,76" fill="#1a1a1a" opacity=".7" transform="translate(0,4)"/>
      <polygon points="262,0 458,0 458,76 392,100 262,76" fill="var(--paper)"/>
    </svg>
    <h2 class="wordmark">DURESK</h2>
    <div class="details">
      <p class="service">PERSONALISED ART</p>
      <p class="specialties">• Portraits • Murals • Fashion Illustration</p>
      <ul class="contact">
        <li>0437 582 190</li>
        <li>duresk@duresk.com.au</li>
        <li>www.duresk.com.au</li>
      </ul>
    </div>
  </section>

</main>
</body>
</html>
```